Silver Heron Coffee Bean Labels

We need a label for a new brand of coffee that we are selling in Portland, Oregon (Coffee Capital). Our company has no current online presence but have some great roasting techniques. We will be roasting our own coffee beans from throughout the world and selling them immediately after roasting causing a super fresh and high quality product.

We will be packaging in brown kraft bags: 3 3/8 X 2.5 x 7.75 inches which is standard for coffee beans.

Also notice on that sample the blue section in the middle has the product name. We want to also make it so that there is a consistent area that we can print OVER the label the name or blend of the coffee.

Our company is called Silver Heron Coffee Roasters. We will want to put silverheronroasters.example on the label someplace (we dont have a site yet but will by launch).

We need to incorporate A Silver Heron into the design. No preferences yet on the style of it.

We want to be a super-premium brand. Sort of like MicroBrew beers. We will sell at Farmers Markets, online, and directly into stores. Image is very important to us.

Labels should be about 3" wide and about 3.75" high.. Perhaps higher if a cool design justifies the height. Again we will be using a brown kraft bag (like grocery bag color) as shown on the sample.

SEE ATTACHED SEVERAL INTERESTING DESIGNS

Target Market(s)

Foodies, Yuppie, Coffee Snob

Industry/Entity Type

It Company

Requirements
Must have
• Location for the product Name to go onto it... We want to use the same labels for our full line. Just printing over it something like "Italian Roast" and a line below saying something like "Bold, Nutty Flavor, blah blah"

Should not have
• Clunkey looking old fonts or things that look homemade.

```html
<!DOCTYPE html>
<html lang="en">
<head>
<meta charset="utf-8">
<title>Silver Heron Coffee Roasters – African Roast Label</title>
<link rel="stylesheet" href="https://fonts.googleapis.com/css2?family=Josefin+Sans:wght@700&display=swap">
<style>
  :root {
    --brand-orange: #f7941d;
    --brand-orange-soft: #fbc27e;
    --ink: #0d0d0d;
    --paper: #ffffff;
  }
  * { margin: 0; padding: 0; box-sizing: border-box; }
  html, body {
    width: 975px;
    height: 1200px;
    overflow: hidden;
    background: var(--paper);
  }
  .label {
    position: relative;
    width: 975px;
    height: 1200px;
    background: var(--paper);
    font-family: "Josefin Sans", sans-serif;
    font-weight: 700;
  }
  .brand-header {
    position: absolute;
    left: 35px;
    top: 35px;
    width: 900px;
    height: 313px;
    background: var(--brand-orange);
  }
  .brand-name {
    position: absolute;
    left: 62px;
    top: 21px;
    color: var(--paper);
    font-size: 51px;
    line-height: 70px;
    letter-spacing: 0.02em;
    text-transform: uppercase;
  }
  .brand-name span { display: block; }
  .brand-mark {
    position: absolute;
    left: 700px;
    top: 150px;
    width: 140px;
    height: 140px;
    border-radius: 50%;
    background: var(--ink);
  }
  .pattern-band {
    position: absolute;
    left: 39px;
    width: 887px;
    height: 79px;
    background: linear-gradient(180deg, var(--brand-orange), var(--brand-orange-soft));
  }
  .pattern-band--top { top: 358px; }
  .pattern-band--bottom {
    top: 1073px;
    background: linear-gradient(0deg, var(--brand-orange), var(--brand-orange-soft));
  }
  .product {
    position: absolute;
    left: 0;
    width: 975px;
    text-align: center;
  }
  .product-name {
    top: 598px;
    color: var(--ink);
    font-size: 92px;
    line-height: 92px;
    letter-spacing: 0.005em;
  }
  .product-notes {
    top: 706px;
    color: var(--brand-orange);
    font-size: 50px;
    line-height: 56px;
    letter-spacing: 0.21em;
    padding-left: 0.21em;
  }
  .site-url {
    position: absolute;
    right: 67px;
    top: 1035px;
    color: var(--brand-orange);
    font-size: 18px;
    letter-spacing: 0.02em;
    text-transform: uppercase;
  }
</style>
</head>
<body>
  <main class="label">
    <header class="brand-header">
      <h1 class="brand-name">
        <span>Silver</span>
        <span>Heron</span>
        <span>Coffee</span>
        <span>Roasters</span>
      </h1>
      <div class="brand-mark" aria-hidden="true"></div>
    </header>

    <div class="pattern-band pattern-band--top" role="img" aria-label="Decorative orange border pattern along the top"></div>

    <h2 class="product product-name">AFRICAN ROAST</h2>
    <p class="product product-notes">BOLD, NUTTY FLAVOR</p>

    <p class="site-url">silverheronroasters.example</p>

    <div class="pattern-band pattern-band--bottom" role="img" aria-label="Decorative orange border pattern along the bottom"></div>
  </main>
</body>
</html>
```